Football/Sports Motivational Poster

Use the picture provided. Crop the lady out to the right. At the top of the poster "Pressure Is A Privilege"
At the bottom of the poster "Prove Them Wrong"
Vertical Poster. Must look Bad Ass! Also include various high res files

```html
<!DOCTYPE html>
<html lang="en">
<head>
<meta charset="utf-8">
<title>Pressure Is A Privilege – Football Motivational Poster</title>
<link rel="stylesheet" href="https://fonts.googleapis.com/css2?family=Russo+One&family=Oswald:wght@500;600;700&display=swap">
<style>
  :root {
    --page-bg: #ffffff;
    --navy-deep: #0c1622;
    --navy: #13243a;
    --navy-mid: #1c3556;
    --band-blue: #28466e;
    --band-light: #3a5f8f;
    --sky: #6fb4f5;
    --sky-pale: #cfe6fb;
    --ice: #f2f6fa;
    --silver: #c9ced4;
    --outline-blue: #2a5fd0;
    --shadow-dark: #081019;
    --photo-grey-light: #d9dcdf;
    --photo-grey-dark: #3d4148;
  }
  * { margin: 0; padding: 0; box-sizing: border-box; }
  html, body {
    width: 1200px; height: 2967px; overflow: hidden;
    background: var(--page-bg);
  }
  .canvas { position: relative; width: 1200px; height: 2967px; }

  .poster {
    position: absolute; left: 90px; top: 823px;
    width: 1020px; height: 1320px; overflow: hidden;
    background: radial-gradient(ellipse at 55% 45%, var(--navy-mid) 0%, var(--navy) 45%, var(--navy-deep) 100%);
    box-shadow: 0 6px 22px rgba(0,0,0,0.45);
  }
  .poster__bands { position: absolute; inset: 0; width: 100%; height: 100%; }

  .photo { position: absolute; }
  .photo--echo {
    left: 120px; top: 300px; width: 360px; height: 800px;
    border-radius: 160px 160px 40px 40px;
    background: linear-gradient(180deg, rgba(120,160,205,0.55) 0%, rgba(90,130,180,0.45) 60%, rgba(60,95,140,0.15) 100%);
  }
  .photo--athlete {
    left: 390px; top: 250px; width: 290px; height: 1010px;
    border-radius: 120px 120px 30px 30px;
    background: linear-gradient(180deg, var(--photo-grey-dark) 0%, var(--photo-grey-light) 22%, #bfc3c8 55%, var(--photo-grey-dark) 100%);
  }

  .headline { position: absolute; left: 0; width: 100%; text-align: center; font-family: "Russo One", sans-serif; line-height: 1; }
  .headline--lead {
    top: 62px; left: -75px; font-size: 96px; letter-spacing: 1px;
    background: linear-gradient(180deg, var(--ice) 0%, var(--sky-pale) 35%, var(--sky) 70%, #4d97e8 100%);
    -webkit-background-clip: text; background-clip: text; color: transparent;
    filter: drop-shadow(3px 4px 0 var(--shadow-dark));
  }
  .headline--main {
    top: 158px; left: -40px; font-size: 150px; letter-spacing: 2px;
    background: linear-gradient(180deg, #ffffff 0%, var(--silver) 45%, #f4f4f4 55%, #dfe3e8 100%);
    -webkit-background-clip: text; background-clip: text; color: transparent;
    -webkit-text-stroke: 3px var(--outline-blue);
    filter: drop-shadow(6px 7px 0 var(--shadow-dark));
  }

  .tagline { position: absolute; font-family: "Oswald", sans-serif; line-height: 1; text-transform: uppercase; }
  .tagline--prove {
    left: 148px; top: 905px; font-size: 176px; font-weight: 600; letter-spacing: -2px;
    background: linear-gradient(180deg, #ffffff 0%, var(--ice) 50%, var(--sky-pale) 100%);
    -webkit-background-clip: text; background-clip: text; color: transparent;
    filter: drop-shadow(3px 4px 0 var(--shadow-dark));
  }
  .tagline--them {
    left: 268px; top: 1050px; font-size: 104px; font-weight: 500; color: var(--ice);
    filter: drop-shadow(3px 3px 0 var(--shadow-dark));
  }
  .tagline--wrong {
    left: 700px; top: 742px; font-size: 212px; font-weight: 700; letter-spacing: -2px;
    transform: translate(-50%, -50%) rotate(-90deg);
    background: linear-gradient(90deg, var(--sky) 0%, #8cc6f8 50%, var(--sky-pale) 100%);
    -webkit-background-clip: text; background-clip: text; color: transparent;
    filter: drop-shadow(5px 5px 0 var(--shadow-dark));
  }
</style>
</head>
<body>
<div class="canvas">
  <section class="poster">
    <svg class="poster__bands" viewBox="0 0 1020 1320" preserveAspectRatio="none" aria-hidden="true">
      <polygon points="0,640 1020,290 1020,560 0,960" fill="var(--band-blue)" opacity="0.75"/>
      <polygon points="0,700 1020,360 1020,420 0,760" fill="var(--band-light)" opacity="0.35"/>
      <polygon points="0,1020 1020,720 1020,820 0,1110" fill="var(--band-blue)" opacity="0.55"/>
      <polygon points="0,1180 1020,930 1020,980 0,1230" fill="var(--band-light)" opacity="0.2"/>
    </svg>

    <div class="photo photo--echo" role="img" aria-label="Faded blue-tinted close-up of the football player, head bowed, as a background echo"></div>
    <div class="photo photo--athlete" role="img" aria-label="Black and white photo of a football player in a white jersey walking with head down, holding a towel and helmet"></div>

    <h1 class="headline headline--lead">PRESSURE IS A</h1>
    <div class="headline headline--main">PRIVILEGE</div>

    <div class="tagline tagline--prove">PROVE</div>
    <div class="tagline tagline--them">THEM</div>
    <div class="tagline tagline--wrong">WRONG</div>
  </section>
</div>
</body>
</html>
```